TuneNest - Music Industry App needs a top quality wordpress homepage

We need a modern responsive wordpress homepage built. Our website will only feature one page with the goal to get people to sign up to our app. A word document has been uploaded outlining the page content/sections.

Once the homepage is finalised, I will also need 2 landing pages built as part of this competition. It will be very similar to the homepage with the same layout etc but just feature different images and content. The homepage is for anyone (artists and venues) to find out about us but the landing pages will be artist or venue specific.

The completed work must be delivered as an exportable file into wordpress and be designed properly so no more work is needed to begin utilising as the actual website. The images used must be setup correctly for speed and quality also.

Target Market(s)

Venues and Artists.

Coding

Coded - Design and coding required

Requirements
Must have
• UPDATE: High Res Logo files attached
• Must be a modern looking website and be responsive. Must look good across all devices from desktop, to mobile and tablet. Needs to be very high quality.
• Please see the attached logo - I am waiting for the final high quality version and will reupload when complete but this will be enough to get you started for now. The website must have a dark base colour and have red/white elements to match the logo. The red colour used MUST match the red colour used in the logo.
• Please have a go at creating it how you think is best and provide feedback from there. I am leaving it very open to the designers so I can get the best website possible and lots of different ideas etc.

```html
<!DOCTYPE html>
<html lang="en">
<head>
<meta charset="utf-8">
<title>TuneNest – Rydeo for Live Music</title>
<link rel="stylesheet" href="https://fonts.googleapis.com/css2?family=Montserrat:wght@400;500;600&family=Open+Sans:wght@400;600;700&display=swap">
<style>
:root{
  --red:#e30613;
  --black:#000;
  --ink:#222;
  --paper:#f3f1f2;
  --card:#fff;
  --muted:#c9c9c9;
  --grey-circle:#333;
  --contact-bg:#2c2c2c;
  --head:"Montserrat",sans-serif;
  --body:"Open Sans",sans-serif;
}
*{box-sizing:border-box;margin:0;padding:0}
html,body{width:1200px;height:3362px;overflow:hidden;background:var(--black)}
body{position:relative;font-family:var(--body);color:#fff}
.abs{position:absolute}
.center{left:0;width:1200px;text-align:center}

/* hero */
.hero-photo{left:0;top:0;width:1200px;height:720px;
  background:radial-gradient(ellipse at 50% 25%,#b3101c 0%,#7d0a14 45%,#3a0508 80%,#000 100%)}
.brand{top:40px;display:flex;flex-direction:column;align-items:center}
.brand-dot{width:92px;height:92px;border-radius:50%;background:var(--red);margin-bottom:8px}
.brand-name{font-family:var(--head);font-weight:500;font-size:46px;color:#fff;line-height:1}
.hero-title{top:262px;font-family:var(--head);font-weight:500;font-size:46px}
.hero-sub{top:332px;font-family:var(--head);font-weight:500;font-size:31px;line-height:36px}
.hero-cta{top:434px;font-family:var(--head);font-weight:500;font-size:22px}
.signup{display:flex;align-items:center;background:#fff;border:none;height:53px;padding:0 8px 0 23px}
.signup .field{flex:1;font-size:15px;color:#444}
.signup .btn{background:var(--red);color:#fff;font-family:var(--head);font-weight:500;font-size:19px;height:41px;display:flex;align-items:center;justify-content:center}
.hero-form{left:353px;top:480px;width:500px}
.hero-form .btn{width:140px}

/* steps */
.section-title{font-family:var(--head);font-weight:500;font-size:30px}
.steps-title{top:798px}
.step{width:190px;text-align:center}
.step-icon{width:96px;height:96px;border-radius:50%;background:var(--grey-circle);margin:0 auto;display:flex;align-items:center;justify-content:center}
.step-num{font-family:var(--head);font-weight:500;font-size:33px;margin-top:20px;line-height:40px}
.step-text{font-size:15px;line-height:23px;color:#ddd;margin-top:6px}

/* why */
.why-band{left:0;top:1240px;width:1200px;height:510px;background:var(--paper)}
.edge{left:0;width:1200px;height:60px}
.edge-top{top:1200px;background:linear-gradient(#000,var(--paper))}
.edge-bottom{top:1735px;background:linear-gradient(var(--paper),#1e1e1e)}
.why-title{top:1302px;color:var(--ink)}
.card{top:1372px;width:225px;height:288px;background:var(--card);text-align:center;color:var(--ink)}
.card-icon{width:80px;height:80px;border-radius:50%;background:#e2e2e2;margin:34px auto 0;display:flex;align-items:center;justify-content:center}
.card-rule{width:22px;height:2px;background:var(--red);margin:36px auto 0}
.card-title{font-family:var(--body);font-weight:600;font-size:18px;margin-top:17px}
.card-text{font-size:14px;line-height:20px;margin:10px auto 0;width:175px;color:#333}

/* venues */
.venues-photo{left:0;top:1790px;width:1200px;height:470px;
  background:linear-gradient(180deg,#1c1c1c 0%,#2a2a2a 45%,#232323 100%)}
.venues-title{left:162px;top:1843px;font-family:var(--body);font-size:27px}
.venue-list{left:168px;top:1900px;list-style:none;font-size:16px;line-height:29.3px;color:#eee}
.venue-list li::before{content:"›";font-weight:700;font-size:22px;margin-right:10px;position:relative;top:1px}
.venue-note{left:168px;top:2060px;width:500px;font-size:14.5px;line-height:19.5px;color:#eee}
.venue-form{left:163px;top:2153px;width:500px}
.venue-form .btn{width:140px}

/* about */
.about-photo{left:0;top:2260px;width:1200px;height:495px;
  background:linear-gradient(180deg,#2a2330 0%,#3a2d4a 25%,#221c27 60%,#1a1a1a 100%)}
.about-title{top:2352px;font-family:var(--head);font-weight:500;font-size:41px}
.about-text{top:2422px;left:280px;width:640px;text-align:center;font-size:14.5px;line-height:23.2px;color:#eee}

/* contact */
.contact{left:0;top:2755px;width:615px;height:506px;background:var(--contact-bg)}
.contact-title{left:159px;top:2808px;font-family:var(--head);font-weight:500;font-size:34px}
.field-line{left:159px;width:391px;border-bottom:1px solid #bbb;font-size:16px;color:#ddd;padding-bottom:4px}
.submit{left:163px;top:3129px;width:153px;height:43px;background:var(--red);font-family:var(--head);font-weight:500;font-size:19px;display:flex;align-items:center;justify-content:center}
.map{left:615px;top:2755px;width:585px;height:506px;background:linear-gradient(135deg,#ececec,#dcdcdc)}

/* footer */
.footer{left:0;top:3261px;width:1200px;height:101px;background:#000;display:flex;align-items:center;justify-content:center;font-family:var(--head);font-size:15px}
</style>
</head>
<body>

<!-- hero -->
<div class="abs hero-photo" role="img" aria-label="Concert crowd with raised hands under red stage lights"></div>
<div class="abs center brand">
  <div class="brand-dot"></div>
  <div class="brand-name">TuneNest</div>
</div>
<h1 class="abs center hero-title">Rydeo for Live Music</h1>
<p class="abs center hero-sub">TuneNest connects venues with artists to<br>make booking gigs simple</p>
<p class="abs center hero-cta">Join Now for FREE</p>
<div class="abs signup hero-form"><span class="field">Email address</span><span class="btn">Join Now</span></div>

<!-- how it works -->
<h2 class="abs center section-title steps-title">How TuneNest Works</h2>

<div class="abs step" style="left:141px;top:886px">
  <div class="step-icon"><svg width="46" height="50" viewBox="0 0 46 50" fill="none" stroke="#e30613" stroke-width="3"><rect x="4" y="6" width="32" height="40" rx="3"/><path d="M12 18h16M12 26h16M12 34h10"/><path d="M30 30l10-14 4 3-10 14-5 2z"/></svg></div>
  <div class="step-num">1</div>
  <div class="step-text">Sign up for free -<br>we never charge<br>venues anything!</div>
</div>
<div class="abs step" style="left:324px;top:886px">
  <div class="step-icon"><svg width="50" height="46" viewBox="0 0 50 46" fill="#e30613"><path d="M10 6l14-4v22a6 6 0 1 1-3-5V9l-8 2v17a6 6 0 1 1-3-5z"/><circle cx="36" cy="12" r="6"/><path d="M26 26h20v6H26zM26 36h20v6H26z"/></svg></div>
  <div class="step-num">2</div>
  <div class="step-text">Search for an<br>artist for your<br>upcoming gigs</div>
</div>
<div class="abs step" style="left:506px;top:886px">
  <div class="step-icon"><svg width="50" height="48" viewBox="0 0 50 48" fill="none" stroke="#e30613" stroke-width="3"><path d="M25 4C13 4 4 12 4 22c0 5 2 9 6 12l-3 10 11-6c2 .5 4 .8 7 .8 12 0 21-8 21-18S37 4 25 4z"/><path d="M15 17h20M15 23h20M15 29h20"/></svg></div>
  <div class="step-num">3</div>
  <div class="step-text">Request a quote and<br>communicate with<br>the artist direct</div>
</div>
<div class="abs step" style="left:689px;top:886px">
  <div class="step-icon"><svg width="58" height="46" viewBox="0 0 58 46" fill="none" stroke="#e30613" stroke-width="3"><rect x="4" y="6" width="30" height="18" rx="2"/><path d="M4 24c6 8 16 10 24 10h8"/><circle cx="44" cy="30" r="10"/><path d="M44 24v12M41 27h5M41 33h5"/></svg></div>
  <div class="step-num">4</div>
  <div class="step-text">The gig is booked in<br>once the quote is<br>accepted and payment<br>provided</div>
</div>
<div class="abs step" style="left:871px;top:886px">
  <div class="step-icon"><svg width="52" height="52" viewBox="0 0 52 52" fill="none" stroke="#e30613" stroke-width="3"><circle cx="26" cy="26" r="22"/><path d="M16 26l7 7 13-14"/></svg></div>
  <div class="step-num">5</div>
  <div class="step-text">Once complete, provide<br>a review and authorise<br>the money to be<br>released to the artist</div>
</div>

<!-- why -->
<div class="abs edge edge-top" role="img" aria-label="Torn paper edge"></div>
<div class="abs why-band"></div>
<h2 class="abs center section-title why-title">Why TuneNest?</h2>

<div class="abs card" style="left:116px">
  <div class="card-icon"><svg width="44" height="40" viewBox="0 0 44 40" fill="none" stroke="#e30613" stroke-width="3"><rect x="3" y="3" width="32" height="30" rx="2"/><path d="M3 10h32"/><circle cx="27" cy="24" r="9"/><path d="M23 24l3 3 5-6M33 31l8 7"/></svg></div>
  <div class="card-rule"></div>
  <div class="card-title">Simple</div>
  <p class="card-text">TuneNest saves time and makes booking gigs simple.</p>
</div>
<div class="abs card" style="left:360px">
  <div class="card-icon"><svg width="50" height="34" viewBox="0 0 50 34" fill="#e30613"><path d="M0 4l10-4 6 16-10 4zM50 4L40 0l-6 16 10 4z"/><path d="M14 8h10l4 3 6-3h5l4 12-14 12-18-10z"/></svg></div>
  <div class="card-rule"></div>
  <div class="card-title">Connect</div>
  <p class="card-text">Find hundreds of talented artists ready to perform at your venue.</p>
</div>
<div class="abs card" style="left:603px">
  <div class="card-icon"><svg width="40" height="46" viewBox="0 0 40 46" fill="#e30613"><path d="M20 0l20 7v14c0 12-9 21-20 25C9 42 0 33 0 21V7z"/><path d="M11 22l7 8 12-15" fill="none" stroke="#fff" stroke-width="4"/></svg></div>
  <div class="card-rule"></div>
  <div class="card-title">Protection</div>
  <p class="card-text">We manage the payment process and provide a money back guarantee.</p>
</div>
<div class="abs card" style="left:847px">
  <div class="card-icon"><svg width="48" height="48" viewBox="0 0 48 48" fill="#e30613"><circle cx="30" cy="12" r="11"/><path d="M30 6v12M27 9h5M27 15h5" stroke="#fff" stroke-width="2"/><path d="M2 30h8l10 4h10l-2 4H18l14 2 12-8 4 2-16 12H10l-8-2z"/></svg></div>
  <div class="card-rule"></div>
  <div class="card-title">Price</div>
  <p class="card-text">Negotiate the best price and don't pay us a cent!</p>
</div>

<!-- venues -->
<div class="abs venues-photo" role="img" aria-label="Dim concert crowd in silhouette"></div>
<div class="abs edge edge-bottom" role="img" aria-label="Torn paper edge"></div>
<h2 class="abs venues-title">Venues</h2>
<ul class="abs venue-list">
  <li>TuneNest is a 100% FREE service for all venues - you pay us nothing!</li>
  <li>Get instant access to hundreds of artists around your local community</li>
  <li>All genres to suit any venue from a pub to a wedding or even a nightclub</li>
  <li>Simple booking process with a money back guarantee</li>
  <li>Communicate directly with the artist and negotiate the price</li>
</ul>
<p class="abs venue-note">TuneNest is not yet ready to host gigs as we're currently working on building our artists lineup. We are launching for venues in Q4 2019. Pre-register now to keep informed and be one</p>
<div class="abs signup venue-form"><span class="field">Email address</span><span class="btn">Pre-Register</span></div>

<!-- about -->
<div class="abs about-photo" role="img" aria-label="Concert crowd lit by purple stage lights"></div>
<h2 class="abs center about-title">About TuneNest</h2>
<p class="abs about-text">We are creating a world class business which will change the way gigs are booked and become the next household name in the app space alongside Rydeo and Roomly. We are average Aussie's with a big dream, living in the Blue Mountains and initially focusing on Sydney and the Australian market. We want to get a small amount of quality artists and venues utilising and loving our service initially to get the formula right before growing the business to become the #1 gig booking platform worldwide. If you are a professional artist or venue based in Sydney, we would love to have you along for the journey.</p>

<!-- contact -->
<div class="abs contact"></div>
<h2 class="abs contact-title">Contact Us</h2>
<div class="abs field-line" style="top:2870px">Name *</div>
<div class="abs field-line" style="top:2913px">Company</div>
<div class="abs field-line" style="top:2963px">E-mail *</div>
<div class="abs field-line" style="top:3007px">Phone Number</div>
<div class="abs field-line" style="top:3050px;height:59px">Message</div>
<div class="abs submit">Submit</div>
<div class="abs map" role="img" aria-label="Street map of the office location with a red pin"></div>

<footer class="abs footer">© 2019 TuneNest&nbsp; All right reserved &nbsp;|&nbsp; Privacy Policy</footer>

</body>
</html>
```